Flyer Design Project

I am opening a yoga studio called Willowmere Yoga .Pilates. Fitness
and require a flyer that will be letterbox dropped. It will two sided - DL size.100mm × 210mm

The studio will offer Vinyasa Flow Yoga and Mat Pilates classes. We aim to enable people to lead healthier, happier lives through improved strength, flexibility and general well being that regular yoga and pilates practice offers.

We offer group classes, private and semi private sessions in yoga and pilates.

it must have the logo on it- I have uploaded the logo in two versions - not sure what will look the best.

pick up one of the colours from the logo as the background colour.

Side one:
Simple and clean with one side showing logo and address details, website and with simple intro about studio (if it fits)

Location: 1st Floor, 17 Larkspur Parade, Tindale, 3286
phone: 0428 596143
www.willowmeretindale.com.au

OPENING OCTOBER

other side - class descriptions and intro offer for new clients
$20 for 7 days of classes
$99 for 1 month unlimited.

Class descriptions:
Vinyasa Flow yoga: A class that flows from pose to pose integrating breath, alignment, strength and power. All levels are catered for in a warm room heated to around 26 degrees. You will leave feeling inspired, empowered and energised.

Mat Pilates: A strong, challenging class integrating the key principles of pilates: concentration, control, centring, precision, flowing movement and breath. Using the core as a focus to develop these principles you will be hooked on the physical freedom you experience post workout:improved strength, flexibility and vitality that pilates offers.

Private and semi Private tuition available.

Target Market(s)

mainly women, athletic, 35-55 age, middle class, well educated

Industry/Entity Type

Fitness

Requirements
Must have
• 2 pages
the logo

Should not have
• no pics

```html
<!DOCTYPE html>
<html lang="en">
<head>
<meta charset="utf-8">
<title>Willowmere Yoga – DL Flyer</title>
<link href="https://fonts.googleapis.com/css2?family=Source+Sans+3:ital,wght@0,400;0,600;0,700;1,700&family=Oswald:wght@600&display=swap" rel="stylesheet">
<style>
  :root {
    --sun: #f7ec23;
    --paper: #ffffff;
    --ink: #111111;
    --bar: #cccccc;
    --bar-edge: #9a9a9a;
  }
  * { margin: 0; padding: 0; box-sizing: border-box; }
  html, body { width: 1200px; height: 848px; overflow: hidden; background: var(--paper); }
  body { position: relative; font-family: "Source Sans 3", "Myriad Pro", sans-serif; color: var(--ink); }

  .flyer-side {
    position: absolute; top: 88px; width: 283px; height: 595px;
    border: 1px solid #333; overflow: hidden;
  }
  .flyer-front { left: 207px; background: var(--sun); }
  .flyer-back { left: 646px; background: var(--paper); }
  .side-waves { position: absolute; inset: 0; width: 100%; height: 100%; }
  .side-waves .band { fill: var(--sun); }
  .side-waves .wash { fill: var(--paper); }

  .brand-name {
    position: absolute; left: 0; right: 0; top: 128px; text-align: center;
    font-weight: 600; font-size: 23px; line-height: 27px; color: var(--ink);
  }

  .contact { position: absolute; left: 0; right: 0; top: 208px; text-align: center; }
  .address { font-size: 18.5px; line-height: 23px; }
  .phone { margin-top: 10px; font-weight: 700; font-size: 21px; display: flex; justify-content: center; align-items: center; gap: 5px; }
  .phone svg { width: 15px; height: 17px; }
  .website { margin-top: 8px; font-weight: 700; font-style: italic; font-size: 14.5px; }

  .intro { position: absolute; left: 17px; width: 249px; top: 353px; font-size: 13.2px; line-height: 16.5px; letter-spacing: 0.15px; text-align: justify; }
  .intro p + p { margin-top: 16px; }

  .opening {
    position: absolute; left: 0; right: 0; bottom: 8px; text-align: center;
    font-family: "Oswald", "Impact", sans-serif; font-weight: 600; font-size: 30px;
    letter-spacing: 0.5px; transform: scaleY(1.15);
  }

  .offer { position: absolute; left: 23px; top: 52px; }
  .offer-title { font-weight: 700; font-style: italic; font-size: 15px; }
  .offer-price { margin-left: 11px; margin-top: 8px; font-weight: 700; font-size: 18.5px; line-height: 28px; }

  .class-block { position: absolute; left: 17px; width: 249px; }
  .class-vinyasa { top: 176px; }
  .class-pilates { top: 339px; }
  .class-title { font-weight: 700; font-style: italic; font-size: 15px; margin-bottom: 9px; }
  .class-text { font-size: 13.2px; line-height: 16.9px; letter-spacing: 0.15px; text-align: justify; text-indent: 10px; }
  .class-note { margin-top: 16px; font-size: 13.2px; text-indent: 10px; }

  .job-bar {
    position: absolute; left: 12px; top: 768px; width: 1149px; height: 50px;
    background: var(--bar); border: 5px solid var(--bar-edge);
    display: flex; align-items: center; padding-left: 22px;
    font-weight: 700; font-size: 17px;
  }
  .job-bar span { font-weight: 400; font-style: italic; margin-left: 5px; }
</style>
</head>
<body>

<section class="flyer-side flyer-front">
  <svg class="side-waves" viewBox="0 0 283 595" preserveAspectRatio="none" aria-hidden="true">
    <path class="wash" d="M0,505 C60,530 120,548 180,544 C230,540 262,546 283,548 V595 H0 Z"/>
  </svg>

  <p class="brand-name">Willowmere Yoga<br>.Pilates. Fitness</p>

  <div class="contact">
    <p class="address">1st Floor, 17 Larkspur Parade,<br>Tindale, 3286</p>
    <p class="phone">
      <svg viewBox="0 0 24 28" aria-hidden="true"><path d="M6 1 L10 7 L7 10 C8 15 11 19 15 21 L18 18 L23 23 L19 27 C9 26 1 16 1 5 Z" fill="#111"/></svg>
      0428 596143
    </p>
    <p class="website">www.willowmeretindale.com.au</p>
  </div>

  <div class="intro">
    <p>The studio will offer Vinyasa Flow Yoga and Mat Pilates classes. We aim to enable people to lead healthier, happier lives through improved strength, flexibility and general well being that regular yoga and pilates practice offers.</p>
    <p>We offer group classes, private and semi private sessions in yoga and pilates.</p>
  </div>

  <div class="opening">OPENING OCTOBER</div>
</section>

<section class="flyer-side flyer-back">
  <svg class="side-waves" viewBox="0 0 283 595" preserveAspectRatio="none" aria-hidden="true">
    <path class="band" d="M0,0 H45 C95,28 185,46 283,40 V158 C200,176 120,140 45,150 C22,153 8,160 0,166 Z"/>
    <path class="band" d="M170,0 H283 V18 C240,14 200,8 170,0 Z"/>
    <path class="band" d="M0,172 C70,160 160,198 283,180 V312 C200,336 100,304 0,322 Z"/>
    <path class="band" d="M0,344 C80,326 180,354 283,320 V595 H0 Z"/>
  </svg>

  <div class="offer">
    <p class="offer-title">Intro offer for new clients:</p>
    <p class="offer-price">$20 for 7 days of classes<br>$99 for 1 month unlimited</p>
  </div>

  <div class="class-block class-vinyasa">
    <h2 class="class-title">Vinyasa Flow yoga:</h2>
    <p class="class-text">A class that flows from pose to pose integrating breath, alignment, strength and power. All levels are catered for in a warm room heated to around 26 degrees. You will leave feeling inspired, empowered and energised.</p>
  </div>

  <div class="class-block class-pilates">
    <h2 class="class-title">Mat Pilates:</h2>
    <p class="class-text">A strong, challenging class integrating the key principles of pilates: concentration, control, centring, precision, flowing movement and breath. Using the core as a focus to develop these principles you will be hooked on the physical freedom you experience post workout:improved strength, flexibility and vitality that pilates offers.</p>
    <p class="class-note">Private and semi Private tuition available.</p>
  </div>
</section>

<footer class="job-bar">Job Type:<span>Flyer Design</span></footer>

</body>
</html>
```